Tandril Energy b-card redesign

I would like to redesign the card (and power point template) for tandril energy. We are a developer/owner/operator of high-tech biomass gasification power plants. We take ag waste like nut shells or fruit pits and convert that into electricity in the 1/2 - 3 MW range. I would like to change our company color from red to golden gate bridge orange (C=0,M=69,,Y=100,B=6).

Tech

```html
<!DOCTYPE html>
<html lang="en">
<head>
<meta charset="utf-8">
<title>Tandril Energy – Business Card</title>
<link href="https://fonts.googleapis.com/css2?family=Jost:wght@400;500;600&display=swap" rel="stylesheet">
<style>
  :root {
    --brand-orange: #f05a14;
    --brand-orange-soft: rgba(240, 90, 20, 0);
    --ink: #111111;
    --paper: #ffffff;
  }
  * { margin: 0; padding: 0; box-sizing: border-box; }
  html, body { width: 1200px; height: 686px; overflow: hidden; background: var(--paper); }
  .card {
    position: relative;
    width: 1200px;
    height: 686px;
    background: var(--paper);
    font-family: "Jost", "Futura", sans-serif;
    color: var(--ink);
    overflow: hidden;
  }
  .brand {
    position: absolute;
    left: 108px;
    top: 128px;
    display: flex;
    align-items: center;
    gap: 16px;
  }
  .brand-name {
    font-size: 50px;
    font-weight: 500;
    letter-spacing: 4px;
    color: var(--ink);
  }
  .brand-dot {
    width: 22px;
    height: 22px;
    border-radius: 50%;
    background: var(--brand-orange);
  }
  .person {
    position: absolute;
    right: 85px;
    top: 146px;
    font-size: 29px;
    display: flex;
    align-items: baseline;
    gap: 12px;
  }
  .person-name { color: var(--brand-orange); font-weight: 600; }
  .person-divider { color: var(--ink); }
  .person-title { color: var(--ink); font-weight: 500; }
  .contact {
    position: absolute;
    right: 85px;
    top: 428px;
    text-align: right;
    font-size: 24px;
    line-height: 36.5px;
  }
  .contact-label { color: var(--brand-orange); }
  .address {
    position: absolute;
    left: 95px;
    top: 501px;
    font-size: 24px;
    line-height: 36.5px;
  }
  .footer-ornament {
    position: absolute;
    left: 0;
    bottom: 0;
    width: 1200px;
    height: 64px;
    background: linear-gradient(to bottom, var(--brand-orange-soft), var(--brand-orange));
  }
</style>
</head>
<body>
  <div class="card">
    <div class="brand">
      <span class="brand-name">Tandril Energy</span>
      <span class="brand-dot"></span>
    </div>

    <div class="person">
      <span class="person-name">Marcus Ellery Dunn</span>
      <span class="person-divider">|</span>
      <span class="person-title">CEO</span>
    </div>

    <div class="contact">
      <div><span class="contact-label">Phone:</span> 415.555.0142</div>
      <div><span class="contact-label">Fax:</span> 415.555.0187</div>
      <div>dunn@tandrilenergy.net</div>
      <div>www.tandrilenergy.net</div>
    </div>

    <div class="address">
      <div>P.O. Box 40218</div>
      <div>Larkspur Bay, CA 94180</div>
    </div>

    <div class="footer-ornament" role="img" aria-label="Orange sweeping arc ornament along the bottom edge"></div>
  </div>
</body>
</html>
```